Steelcrest Process Systems. Needs a Business Card Design

We need a business card design for an engineering company which supplies industrial components (pumps, compressors, mechanical seals) provides repairs and services for above mentioned equipments. We offer a uniqe engineering solutions which help our customers to increase the productivness of their manufacturings, and energy savings.

Target Market(s)

Chemical and energy plants, refineries. Food industry and private consumers in a less.

Industry/Entity Type

Business

Contact Information for Business Card

Stylish and sleek design oriented on industrial area.

Requirements
Should not have
• company name shortening

```html
<!DOCTYPE html>
<html lang="en">
<head>
<meta charset="utf-8">
<title>Steelcrest Process Systems — Business Cards</title>
<link href="https://fonts.googleapis.com/css2?family=Tinos:wght@400;700&family=Nunito:wght@800&display=swap" rel="stylesheet">
<style>
  :root {
    --backdrop: #e6e5e7;
    --paper: #ffffff;
    --violet: #341a63;
    --violet-soft: #4a3278;
    --orange: #e8643a;
    --red-line: #d8432b;
    --gold: #f0a531;
    --yellow: #f5c55a;
    --ink-light: #f2eff8;
  }
  * { box-sizing: border-box; margin: 0; padding: 0; }
  html, body { width: 1200px; height: 800px; overflow: hidden; }
  body {
    background: var(--backdrop);
    font-family: "Tinos", "Times New Roman", serif;
    position: relative;
  }
  .card {
    position: absolute;
    width: 520px;
    height: 297px;
    background: var(--paper);
    overflow: hidden;
    box-shadow: 0 10px 28px rgba(0,0,0,0.12);
  }
  .card-front { left: 60px; top: 252px; }
  .card-back { left: 620px; top: 252px; }
  .card-art { position: absolute; inset: 0; width: 100%; height: 100%; }

  .card-title {
    position: absolute;
    color: var(--ink-light);
    font-size: 19px;
    font-weight: 400;
    white-space: nowrap;
  }
  .card-title .accent { color: var(--gold); font-weight: 700; }
  .card-title-rule {
    position: absolute;
    height: 4px;
    background: var(--red-line);
  }

  /* front card */
  .card-front .card-title { left: 26px; top: 30px; }
  .card-front .card-title-rule { left: 34px; top: 64px; width: 220px; }
  .offer {
    position: absolute;
    left: 26px;
    top: 120px;
    color: var(--ink-light);
  }
  .offer-heading { font-size: 21px; font-weight: 700; }
  .offer-heading .accent { color: var(--gold); font-weight: 400; }
  .offer-list { font-size: 16px; line-height: 1.25; margin-top: 4px; }

  /* name block: dot sits above, right-aligned, never over the text */
  .brand-name {
    position: absolute;
    font-family: "Nunito", "Arial", sans-serif;
    font-weight: 800;
    font-size: 15px;
    color: var(--violet-soft);
    white-space: nowrap;
    display: flex;
    flex-direction: column;
    align-items: flex-end;
    gap: 8px;
  }
  .brand-dot {
    width: 22px; height: 22px; border-radius: 50%;
    background: var(--orange);
    flex: none;
    margin-right: 30px;
  }
  .card-front .brand-name { right: 12px; top: 160px; }

  /* back card */
  .card-back .card-title { right: 24px; top: 22px; }
  .contact-list {
    position: absolute;
    left: 40px;
    top: 80px;
    list-style: none;
    color: var(--ink-light);
    font-size: 15px;
    line-height: 1.3;
  }
  .contact-list li { padding-left: 42px; position: relative; }
  .contact-icon {
    position: absolute;
    left: 0; top: 0;
    width: 26px; height: 26px;
  }
  .website {
    position: absolute;
    left: 40px;
    top: 244px;
    color: var(--ink-light);
    font-size: 15px;
    padding-left: 42px;
  }
  .website .contact-icon { top: -3px; width: 22px; height: 22px; }
  .card-back .brand-name { right: 16px; top: 176px; }
</style>
</head>
<body>

  <!-- Front: products & services -->
  <section class="card card-front" aria-label="Business card front">
    <svg class="card-art" viewBox="0 0 520 297" aria-hidden="true">
      <polygon points="0,0 305,0 268,297 0,297" fill="var(--violet)"/>
    </svg>
    <h1 class="card-title">(<span class="accent">Steelcrest</span> Process Systems)</h1>
    <div class="card-title-rule"></div>
    <div class="offer">
      <p class="offer-heading">Our <span class="accent">Product &amp; Service</span></p>
      <p class="offer-list">Pumps, Compressors,<br>Mechanical seals</p>
    </div>
    <div class="brand-name"><span class="brand-dot"></span>Steelcrest Process Systems</div>
  </section>

  <!-- Back: contacts -->
  <section class="card card-back" aria-label="Business card back">
    <svg class="card-art" viewBox="0 0 520 297" aria-hidden="true">
      <polygon points="0,0 520,0 520,60 200,240 0,240" fill="var(--violet-soft)"/>
      <polygon points="520,60 520,74 222,240 200,240" fill="var(--orange)"/>
      <rect x="340" y="56" width="180" height="6" fill="var(--orange)"/>
      <path d="M0,240 H250 a14,14 0 0 1 0,28 H0 Z" fill="var(--orange)"/>
      <polygon points="0,268 210,268 185,297 0,297" fill="var(--violet-soft)"/>
      <rect x="345" y="262" width="200" height="24" rx="12" fill="var(--yellow)"/>
    </svg>
    <h1 class="card-title">(<span class="accent">Steelcrest</span> Process Systems)</h1>
    <ul class="contact-list">
      <li>
        <svg class="contact-icon" viewBox="0 0 28 28" aria-hidden="true">
          <circle cx="14" cy="14" r="13" fill="var(--ink-light)"/>
          <path d="M7 14 L14 8 L21 14 M9 13 V20 H19 V13" fill="none" stroke="var(--violet-soft)" stroke-width="2" stroke-linejoin="round"/>
        </svg>
        Address / Location
      </li>
      <li>Your email</li>
      <li>Telephone</li>
      <li>Fax</li>
    </ul>
    <p class="website">
      <svg class="contact-icon" viewBox="0 0 24 24" aria-hidden="true">
        <circle cx="12" cy="12" r="10" fill="none" stroke="var(--ink-light)" stroke-width="1.8"/>
        <ellipse cx="12" cy="12" rx="4.5" ry="10" fill="none" stroke="var(--ink-light)" stroke-width="1.5"/>
        <line x1="2" y1="12" x2="22" y2="12" stroke="var(--ink-light)" stroke-width="1.5"/>
      </svg>
      www.yourwebsite.com
    </p>
    <div class="brand-name"><span class="brand-dot"></span>Steelcrest Process Systems</div>
  </section>

</body>
</html>
```